Beauty Studio Business Card Design

its a new business & I want something different and classy
the strips are part of my decor

Target Market(s)

young girls and mature women

Industry/Entity Type

Business

Contact Information for Business Card

Frae-la-mu 26 0459817362 ABN # all on the front
address on the back + apt times & maybe my name
I would like black & white strips & fancy font with a fancy border around Frae-la-mu

```html
<!DOCTYPE html>
<html lang="en">
<head>
<meta charset="utf-8">
<title>Frae-la-mu Business Card</title>
<link href="https://fonts.googleapis.com/css2?family=Cinzel:wght@400&display=swap" rel="stylesheet">
<style>
  :root {
    --page-bg: #e9e7e4;
    --card-black: #141212;
    --card-white: #ffffff;
    --ink-light: #f2efe9;
    --ink-dark: #111111;
    --stripe-black: #0e0d0d;
    --stripe-white: #f4f4f2;
  }
  * { margin: 0; padding: 0; box-sizing: border-box; }
  html, body {
    width: 1200px;
    height: 844px;
    overflow: hidden;
    background: var(--page-bg);
  }
  .canvas {
    position: relative;
    width: 1200px;
    height: 844px;
    display: flex;
    align-items: center;
    justify-content: center;
    gap: 60px;
    font-family: "Cinzel", serif;
  }
  .card {
    position: relative;
    width: 520px;
    height: 297px;
    overflow: hidden;
    box-shadow: 0 6px 18px rgba(0,0,0,0.22);
  }

  /* Front */
  .card-front { background: var(--card-black); color: var(--ink-light); }
  .front-panel {
    position: absolute;
    left: 0; top: 0;
    width: 290px; height: 100%;
    display: flex;
    flex-direction: column;
    align-items: center;
    padding-top: 42px;
  }
  .decor-stripes {
    position: absolute;
    left: 290px; top: 0;
    width: 230px; height: 100%;
    background: repeating-linear-gradient(
      90deg,
      var(--stripe-black) 0 6px,
      var(--stripe-white) 6px 12px
    );
  }
  .brand-name {
    display: flex;
    align-items: center;
    gap: 10px;
    font-size: 27px;
    letter-spacing: 2px;
    text-transform: uppercase;
  }
  .brand-dot {
    width: 10px; height: 10px;
    border-radius: 50%;
    background: currentColor;
  }
  .holder-name {
    margin-top: 48px;
    font-size: 21px;
    letter-spacing: 1px;
    text-transform: uppercase;
  }
  .holder-phone {
    margin-top: 6px;
    font-size: 16px;
    letter-spacing: 1px;
  }
  .abn-line {
    margin-top: 22px;
    font-size: 14px;
    letter-spacing: 1px;
  }

  /* Back */
  .card-back { background: var(--card-white); color: var(--ink-dark); }
  .appointment-field {
    position: absolute;
    left: 28px;
    font-size: 15px;
    letter-spacing: 1px;
    text-transform: uppercase;
  }
  .appointment-field .field-line {
    display: block;
    margin-top: 4px;
    height: 3px;
    background: var(--ink-dark);
  }
  .field-name { top: 128px; width: 330px; }
  .field-time { top: 192px; width: 300px; }
  .back-contact {
    position: absolute;
    right: 24px; top: 34px;
    width: 170px;
    text-align: center;
  }
  .back-contact .brand-name {
    justify-content: center;
    font-size: 19px;
    letter-spacing: 1px;
  }
  .back-contact .brand-dot { width: 8px; height: 8px; }
  .address {
    margin-top: 14px;
    font-style: normal;
    font-size: 13px;
    line-height: 1.3;
    text-transform: uppercase;
    letter-spacing: 0.5px;
  }
</style>
</head>
<body>
  <main class="canvas">
    <section class="card card-front" aria-label="Business card front">
      <div class="front-panel">
        <div class="brand-name"><span class="brand-dot"></span>Frae-la-mu</div>
        <p class="holder-name">Mara Ellis</p>
        <p class="holder-phone">000.0000.0000</p>
        <p class="abn-line">26 0459817362 ABN #</p>
      </div>
      <div class="decor-stripes"></div>
    </section>

    <section class="card card-back" aria-label="Business card back">
      <div class="appointment-field field-name">Name:<span class="field-line"></span></div>
      <div class="appointment-field field-time">Apointment Time:<span class="field-line"></span></div>
      <div class="back-contact">
        <div class="brand-name"><span class="brand-dot"></span>Frae-la-mu</div>
        <address class="address">
          Mara Ellis<br>
          000 Harbour Lane<br>
          Tide Point SA 5000<br>
          Australia
        </address>
      </div>
    </section>
  </main>
</body>
</html>
```